Paper wrap to go around yoga mat

We are wanting a design for paper wrap to go around a kids yoga mat - 24x35cm. I definitely want the logo incorporated into the wrap in a prominent position.
I also have some photos and text that I would like to be used.
As you will see I have uploaded a variety of photos - not all need to be used and it may be that none get used depending on the design. I was thinking of having a blackboard looking background but open to your creative ideas.
I have also included a document with the text for the paper - there is texts for the front and the back of the paper which is highlighted in yellow.
THANK YOU!
Young Kids and parents
- I've used a Tumble fox font on the logo but I would like something simple but playful and cute

```html
<!DOCTYPE html>
<html lang="en">
<head>
<meta charset="utf-8">
<title>tinystretch – yoga mat wrap</title>
<link href="https://fonts.googleapis.com/css2?family=Short+Stack&display=swap" rel="stylesheet">
<style>
  :root{
    --page:#ffffff;
    --lime:#b8d432;
    --sky:#1aa3e0;
    --magenta:#e6157f;
    --orange:#f39200;
    --ink:#4a4a4a;
    --ink-dark:#2b2b2b;
    --paper:#ffffff;
  }
  *{margin:0;padding:0;box-sizing:border-box;}
  html,body{width:1200px;height:1000px;overflow:hidden;background:var(--page);}
  body{font-family:"Short Stack", "Comic Sans MS", cursive;color:var(--ink);position:relative;}

  .wrap-sheet{position:absolute;left:254px;top:30px;width:691px;height:940px;border:1px solid #ddd;overflow:hidden;}
  .wrap-sheet__bg{position:absolute;inset:0;width:100%;height:100%;}

  .brand{position:absolute;left:0;width:346px;top:80px;text-align:center;}
  .brand__dot{display:block;width:144px;height:144px;margin:0 auto;border:5px solid var(--ink-dark);border-radius:50%;}
  .brand__name{display:block;margin-top:26px;font-size:30px;line-height:1;color:var(--ink-dark);font-weight:400;}

  .welcome{position:absolute;left:0;width:346px;text-align:center;}
  .welcome--title{top:338px;font-size:18px;line-height:28px;}
  .welcome--tribe{top:442px;font-size:17px;line-height:27px;}
  .welcome--gift{top:629px;font-size:17px;line-height:27px;}
  .accent-pink{color:var(--magenta);}
  .accent-orange{color:var(--orange);}
  .accent-green{color:var(--lime);}
  .accent-blue{color:var(--sky);}

  .care{position:absolute;left:362px;width:329px;font-size:14.5px;line-height:22px;}
  .care__heading{display:block;text-decoration:underline;}
  .care--tips{top:84px;}
  .care--tips .care__heading{color:var(--lime);}
  .care--wash{top:254px;}
  .care--wash .care__heading{color:var(--orange);}
  .care--store{top:563px;}
  .care--store .care__heading{color:var(--magenta);}

  .build-label{position:absolute;left:567px;top:930px;}
  .build{position:absolute;left:520px;top:722px;font-size:16px;color:var(--lime);}
  .build__arrow{position:absolute;left:495px;top:718px;}

  .photo{position:absolute;}
  .photo--blocks{left:380px;top:764px;width:173px;height:116px;background:linear-gradient(135deg,#f3f3f3,#e8c13a 35%,#3b8fd6 60%,#d8322f 85%,#f3f3f3);}
  .photo--child{left:83px;top:740px;width:290px;height:200px;background:linear-gradient(180deg,#ffffff 0%,#f2e6e0 45%,#c8e57a 70%,#d7b7d8 100%);}
</style>
</head>
<body>
  <main class="wrap-sheet">
    <svg class="wrap-sheet__bg" viewBox="0 0 500 680" preserveAspectRatio="none" aria-hidden="true">
      <rect width="500" height="680" fill="var(--lime)"/>
      <path d="M0 62 C120 -6 340 -6 500 98 L500 122 C330 22 120 28 0 98 Z" fill="var(--sky)"/>
      <path d="M0 96 C120 28 330 22 500 120 L500 612 C380 652 220 682 0 628 Z" fill="var(--paper)"/>
      <path d="M170 680 C300 670 420 640 500 612 L500 650 C430 668 340 680 300 680 Z" fill="var(--magenta)"/>
    </svg>

    <div class="brand">
      <span class="brand__dot"></span>
      <span class="brand__name">tinystretch</span>
    </div>

    <p class="welcome welcome--title">Congratulations and Welcome<br>to the tinystretch family!</p>
    <p class="welcome welcome--tribe">We are so excited to have <span class="accent-pink">you</span><br>as part of our tribe as you<br>start your journey<br>towards greater harmony<br>of the <span class="accent-orange">mind</span>, <span class="accent-green">body</span> and <span class="accent-blue">spirit</span></p>
    <p class="welcome welcome--gift">The profound power<br>of yoga<br>is truly a gift that keeps<br>on giving!</p>

    <section class="care care--tips">
      <span class="care__heading">Using tips:</span>
      Lightly spray water on the<br>top surface of the mat before<br>practice to prevent sliding if you<br>have dry hands and feet.
    </section>
    <section class="care care--wash">
      <span class="care__heading">Care instruction:</span>
      Hand wash: wipe with clean wet<br>towel.<br>Machine washable: wash separate<br>on gentle cycle in cold water<br>(no bleach)<br>along with detergent, hang to dry.<br>(DO NOT put in dryer)<br>To speed up drying, wrap mat<br>in a towel and squeeze out<br>excess water.
    </section>
    <section class="care care--store">
      <span class="care__heading">Storage:</span>
      Wrap the mat with printing side<br>out, stored in cool and dry place<br>when not in use, avoid sun exposure.
    </section>

    <svg class="build__arrow" width="50" height="40" viewBox="0 0 50 40" aria-hidden="true">
      <path d="M44 12 C30 -2 10 4 8 30" fill="none" stroke="#999" stroke-width="1.5"/>
      <path d="M2 22 L8 32 L14 23" fill="none" stroke="#999" stroke-width="1.5"/>
    </svg>
    <span class="build" style="left:567px;top:730px;position:absolute;">Build me up</span>

    <div class="photo photo--blocks" role="img" aria-label="Photo of a colourful building-block mat with toy balls"></div>
    <div class="photo photo--child" role="img" aria-label="Photo of a young girl stretching on a lilac yoga mat"></div>
  </main>
</body>
</html>
```